Pivots & Treads .com

This website is simple!!!
Landing page background image should capture the customers attention!!! We will provide a image as a example of what we like. The purpose for this website is to provide customers with a clean easy way to request a quote for industrial casters and wheels by OEM’s as well as maintenance departments worldwide. Please see if you can follow our thought process below.
Customer comes to website, they are invited to Request a Quote by providing us with Manufacturer Name, Manufacturers Part # and quantity needed.
If this is not known the customer will complete will WP conversation format form answering about 10 questions
Or
Look up the part number in one of the 8 to 12 catalogs located in the Flippin Book format on our catalog page, or equal plug in .
When the client request a quote a account page will pop up request The following:
Clients first and last name
Email address
And optional questions
Company name and best contact number.
Once this is complete customer will hit SUBMIT.
The customers request will be in system. A email will be sent to Customer service notifying us the Quote Request has been made.
We will then build a quote for the customer with a good, better and best options. Customers Request a Quote submission may have more than one caster or wheel requested at a time, so website must allow this.
When the customer comes back into website there email address will come up as the account name and request a password be made for them. This will allow them to store quotes in their account for future needs. If quote is older than 30 day the system will trigger a button at the bottom of the quote for resubmit Request for updated quote.
Once customer reviews quote the quote can be Converted to order within the website.
Once Converted the system will send us a email and order will be processed.
We will need a Chat program that will text to CS the questions.
You will need to have high quality graphic design skills on your team.
We have found 2 plugins that would work nicely with our new website Flippin books to showcase our catalogs for customers to research and WPForms conversation forms to complete request for quote form.
Just Ideas:
Very very ghosted caster blueprint in white background but very very ghosted or the icon just idea
We have never had a font used we like
Grayscale every except for rubber on wheels and logo icon
Website should have hamburger menu on left
Website should hav responsive deign
Account head on right side
Has anyone read the brief from top to bottom and the updates, I’m seeing a lot of duplicates of the website I posted in images I want a clean website With lite backgrand with the poly being definite colors on each wheel I added a green yellow and red image has anyone looked at that Just a question?
Went on vacation/holiday

```html
<!DOCTYPE html>
<html lang="en">
<head>
<meta charset="utf-8">
<title>Pivots &amp; Treads .com — Casters and Wheels</title>
<link rel="stylesheet" href="https://fonts.googleapis.com/css2?family=Oswald:wght@500;600;700&family=Poppins:wght@400;500;600&display=swap">
<style>
:root{
  --navy:#1c2c78;
  --navy-deep:#121d55;
  --brand:#2b48b8;
  --sky:#4d8fe6;
  --ink:#2a2f3d;
  --muted:#8a8f9c;
  --field:#eef0f4;
  --band:#eeeff2;
  --white:#ffffff;
}
*{margin:0;padding:0;box-sizing:border-box}
html,body{width:1200px;height:3008px;overflow:hidden;background:var(--white)}
body{position:relative;font-family:"Poppins",sans-serif;color:var(--ink)}
.abs{position:absolute}
.display{font-family:"Oswald",sans-serif;text-transform:uppercase;letter-spacing:.5px}

/* hero */
.hero{left:0;top:0;width:1200px;height:780px;background:linear-gradient(135deg,var(--navy-deep) 0%,var(--navy) 55%,#2a3f9e 100%);clip-path:polygon(0 0,1200px 0,1200px 600px,0 780px)}
.hero-photo{left:430px;top:140px;width:740px;height:540px;border-radius:40% 20% 30% 30%;background:radial-gradient(ellipse at 60% 55%,#7b8595 0%,#4d5a78 40%,rgba(40,55,120,0) 72%)}
.brand-name{font-family:"Poppins",sans-serif;font-weight:600;font-size:19px;color:var(--white);display:flex;align-items:center;gap:10px}
.brand-dot{width:14px;height:14px;border-radius:50%;background:var(--white)}
.top-icons{right:50px;top:44px;display:flex;gap:22px}
.welcome{left:60px;top:184px;font-family:"Oswald",sans-serif;font-weight:600;font-size:22px;color:var(--white);display:flex;align-items:center;gap:14px;letter-spacing:1px}
.welcome::before{content:"";width:40px;height:3px;background:var(--white)}
.hero-title{left:60px;top:214px;font-family:"Oswald",sans-serif;font-weight:700;font-size:118px;line-height:1.02;color:var(--white);text-transform:uppercase}
.hero-title .accent{color:var(--sky)}
.scroll-cue{left:14px;top:580px;transform:rotate(-90deg);transform-origin:left top;font-size:11px;color:var(--white);letter-spacing:2px;display:flex;align-items:center;gap:10px}

/* process */
.process{left:110px;top:790px;width:460px;height:260px}
.step-label{font-family:"Oswald",sans-serif;font-weight:500;font-size:14px;color:var(--ink);text-transform:uppercase;line-height:1.25}
.hub-name{left:160px;top:70px;width:150px;height:110px;display:flex;align-items:center;justify-content:center;text-align:center;font-family:"Poppins",sans-serif;font-weight:600;font-size:19px;color:var(--brand)}
.solutions{left:740px;top:822px}
.solutions h2{font-family:"Oswald",sans-serif;font-weight:600;font-size:42px;line-height:1.1;color:var(--brand);text-transform:uppercase}
.btn{display:inline-flex;align-items:center;justify-content:center;height:38px;padding:0 30px;border-radius:19px;font-size:13px;font-weight:600;text-transform:uppercase;letter-spacing:.5px}
.btn-solid{background:var(--brand);color:var(--white)}
.btn-line{border:2px solid var(--brand);color:var(--brand);background:var(--white)}
.btn-row{display:flex;gap:16px;margin-top:26px}

/* resubmit band */
.band{left:0;top:1130px;width:1200px;height:540px;background:var(--band)}
.section-title{font-family:"Oswald",sans-serif;font-weight:600;font-size:40px;line-height:1.12;color:var(--brand);text-transform:uppercase}
.band-title{left:0;top:1195px;width:1200px;text-align:center}
.cards{left:72px;top:1340px;display:flex;gap:24px}
.card{width:246px;height:290px;background:var(--white);box-shadow:0 6px 18px rgba(20,30,70,.08);text-align:center}
.card-photo{margin:16px auto 0;width:170px;height:150px;border-radius:8px}
.card h3{margin-top:18px;font-family:"Oswald",sans-serif;font-weight:600;font-size:16px;text-transform:uppercase}
.card .price{margin-top:4px;font-size:14px;color:var(--muted)}
.card .link{margin-top:8px;display:inline-block;font-size:11px;font-weight:600;color:var(--sky);text-transform:uppercase;border-bottom:1px solid var(--sky)}

/* about */
.about{left:60px;top:1740px;width:440px}
.about p{margin-top:22px;font-size:13px;line-height:1.75;color:#555a66}
.about .btn{margin-top:28px;height:34px;padding:0 22px;font-size:11px}
.about-photo{left:540px;top:1720px;width:560px;height:420px;border-radius:30px;background:radial-gradient(ellipse at 45% 55%,#3f7f4e 0%,#4b5460 45%,#c9ccd2 75%,rgba(255,255,255,0) 100%)}

/* quote */
.quote-band{left:0;top:2120px;width:1200px;height:500px;background:var(--band);clip-path:polygon(0 60px,1200px 0,1200px 500px,0 500px)}
.footer-band{left:0;top:2480px;width:1200px;height:528px;background:var(--brand);clip-path:polygon(0 80px,1200px 0,1200px 528px,0 528px)}
.quote-card{left:140px;top:2175px;width:420px;height:450px;background:var(--white);border-radius:6px;box-shadow:0 10px 30px rgba(20,30,70,.14);padding:34px 40px}
.quote-card h2{text-align:center;font-family:"Oswald",sans-serif;font-weight:600;font-size:32px;color:var(--brand);text-transform:uppercase}
.field{margin-top:20px}
.field label{display:block;font-size:11px;font-weight:600;color:var(--ink);margin-bottom:8px}
.field .input{height:34px;border-radius:17px;background:var(--field);font-size:11px;color:var(--muted);padding:0 16px;display:flex;align-items:center;justify-content:space-between}
.quote-card .btn{width:100%;margin-top:22px;height:36px}
.older{left:628px;top:2230px}
.older h2{font-size:46px;line-height:1.1}
.older .btn{margin-top:26px;height:34px;padding:0 26px;font-size:11px}

/* footer */
.foot-brand{left:150px;top:2770px}
.foot-col{top:2712px;color:var(--white)}
.foot-col h4{font-family:"Oswald",sans-serif;font-weight:600;font-size:15px;text-transform:uppercase;margin-bottom:12px}
.foot-col li{list-style:none;font-size:12px;line-height:1.9;opacity:.9}
.socials{display:flex;gap:12px}
.socials span{width:30px;height:30px;border-radius:50%;border:1.5px solid rgba(255,255,255,.8)}
.copyright{left:0;top:2955px;width:1200px;text-align:center;font-size:12px;color:var(--white);opacity:.85}
.chat{left:1138px;top:2942px;width:42px;height:42px;border-radius:50%;background:var(--white);display:flex;align-items:center;justify-content:center}
</style>
</head>
<body>

<!-- hero -->
<section class="abs hero">
  <div class="abs hero-photo" role="img" aria-label="Three industrial swivel casters with red, blue and green wheels"></div>
  <div class="abs brand-name" style="left:60px;top:38px"><span class="brand-dot"></span>Pivots &amp; Treads .com</div>
  <div class="abs top-icons">
    <svg width="18" height="18" viewBox="0 0 18 18" fill="#fff"><circle cx="9" cy="5" r="4"/><path d="M1 17c0-4 4-6 8-6s8 2 8 6z"/></svg>
    <svg width="20" height="18" viewBox="0 0 20 18" fill="none" stroke="#fff" stroke-width="1.8"><path d="M1 1h3l2 11h11l2-8H5"/><circle cx="8" cy="16" r="1.3" fill="#fff"/><circle cx="16" cy="16" r="1.3" fill="#fff"/></svg>
    <svg width="20" height="18" viewBox="0 0 20 18" stroke="#fff" stroke-width="2"><path d="M1 3h18M1 9h18M1 15h18"/></svg>
  </div>
  <div class="abs welcome">WELCOME TO</div>
  <h1 class="abs hero-title">Casters<br><span class="accent">And</span><br>Wheels</h1>
  <div class="abs scroll-cue">
    <svg width="12" height="18" viewBox="0 0 12 18" fill="none" stroke="#fff" stroke-width="1.5"><rect x="1" y="1" width="10" height="16" rx="5"/><path d="M6 5v3"/></svg>
    SCROLL
  </div>
</section>

<!-- process -->
<div class="abs process">
  <svg class="abs" style="left:0;top:0" width="460" height="260" viewBox="0 0 460 260">
    <circle cx="235" cy="125" r="95" fill="none" stroke="#dfe5f5" stroke-width="2"/>
    <path d="M140 125a95 95 0 0 1 40-78" fill="none" stroke="#4d8fe6" stroke-width="3"/>
    <circle cx="150" cy="82" r="16" fill="#4d8fe6"/>
    <path d="M144 82h12M150 76v12" stroke="#fff" stroke-width="2"/>
    <circle cx="316" cy="135" r="16" fill="#4d8fe6"/>
    <path d="M309 135l5 5 9-10" stroke="#fff" stroke-width="2" fill="none"/>
    <circle cx="200" cy="212" r="16" fill="#4d8fe6"/>
    <path d="M193 207h14v10h-14z M193 207l7 5 7-5" stroke="#fff" stroke-width="1.6" fill="none"/>
  </svg>
  <div class="abs step-label" style="left:60px;top:24px">Request a<br>Quote</div>
  <div class="abs step-label" style="left:346px;top:150px">Convert a Quote<br>to Order</div>
  <div class="abs step-label" style="left:230px;top:220px">Receive a<br>Quote</div>
  <div class="abs hub-name">Pivots &amp; Treads .com</div>
</div>

<div class="abs solutions">
  <h2>#1 Solutions for all<br>your applications</h2>
  <div class="btn-row">
    <span class="btn btn-solid">Submit Quote</span>
    <span class="btn btn-line">Catalog</span>
  </div>
</div>

<!-- resubmit -->
<div class="abs band"></div>
<h2 class="abs section-title band-title">Resubmit request for<br>updated quote</h2>
<div class="abs cards">
  <article class="card">
    <div class="card-photo" role="img" aria-label="Black swivel caster with brake" style="background:radial-gradient(circle,#3b3f47 0%,#c7cad0 70%,#fff 100%)"></div>
    <h3>Product Heading Here</h3><div class="price">$12.00</div><span class="link">Resubmit Quote</span>
  </article>
  <article class="card">
    <div class="card-photo" role="img" aria-label="Green wheel rigid caster" style="background:radial-gradient(circle,#3f6b4c 0%,#c7cad0 70%,#fff 100%)"></div>
    <h3>Product Heading Here</h3><div class="price">$12.00</div><span class="link">Resubmit Quote</span>
  </article>
  <article class="card">
    <div class="card-photo" role="img" aria-label="Red wheel swivel caster with brake" style="background:radial-gradient(circle,#9b3a34 0%,#c7cad0 70%,#fff 100%)"></div>
    <h3>Product Heading Here</h3><div class="price">$12.00</div><span class="link">Resubmit Quote</span>
  </article>
  <article class="card">
    <div class="card-photo" role="img" aria-label="Blue wheel swivel caster" style="background:radial-gradient(circle,#2f4a8c 0%,#c7cad0 70%,#fff 100%)"></div>
    <h3>Product Heading Here</h3><div class="price">$12.00</div><span class="link">Resubmit Quote</span>
  </article>
</div>

<!-- about -->
<section class="abs about">
  <h2 class="section-title">About<br>Caster Wheels</h2>
  <p>We supply industrial casters and wheels to equipment makers and maintenance teams around the world. Send us a part number and quantity, and our team will return a quote with good, better and best options for your application, ready to convert into an order.</p>
  <span class="btn btn-line">Read More</span>
</section>
<div class="abs about-photo" role="img" aria-label="Two heavy duty rigid casters with green and black wheels"></div>

<!-- quote -->
<div class="abs quote-band"></div>
<div class="abs footer-band"></div>
<form class="abs quote-card">
  <h2>Request a Quote</h2>
  <div class="field"><label>Manufacturer Name</label><div class="input">Enter Name</div></div>
  <div class="field"><label>Manufacturers Part #</label><div class="input">Enter part #</div></div>
  <div class="field"><label>Quantity needed</label><div class="input">0
    <svg width="10" height="8" viewBox="0 0 10 8" fill="#8a8f9c"><path d="M0 0h10L5 7z"/></svg></div></div>
  <span class="btn btn-solid">Submit Quote</span>
</form>
<div class="abs older">
  <h2 class="section-title">If quote is older<br>than 30 day</h2>
  <span class="btn btn-line">Resubmit</span>
</div>

<!-- footer -->
<div class="abs foot-brand brand-name"><span class="brand-dot"></span>Pivots &amp; Treads .com</div>
<nav class="abs foot-col" style="left:610px">
  <h4>Quick Links</h4>
  <ul><li>Home</li><li>Resubmit</li><li>Request Quote</li><li>About</li><li>Contact Us</li></ul>
</nav>
<nav class="abs foot-col" style="left:780px">
  <h4>Solutions</h4>
  <ul><li>Request a Quote</li><li>Receive a Quote</li><li>Convert a Quote to Order</li></ul>
</nav>
<div class="abs foot-col" style="left:960px">
  <h4>Stay Connected</h4>
  <div class="socials"><span></span><span></span><span></span><span></span></div>
</div>
<div class="abs copyright">© Copyright 2021 All Rights Reserved</div>
<div class="abs chat">
  <svg width="20" height="18" viewBox="0 0 20 18" fill="#2b48b8"><path d="M2 1h16a1 1 0 0 1 1 1v10a1 1 0 0 1-1 1H8l-5 4v-4H2a1 1 0 0 1-1-1V2a1 1 0 0 1 1-1z"/></svg>
</div>

</body>
</html>
```